Helicopter company requires newspaper ad

"Ridgeline Aviation" is an agricultural helicopter company based in Victoria, Australia. We need an advert design for use in newspapers and also possibly social media. Our company specialises in using a helicopter for various agricultural work such as Spraying weeds ("Cropdusting"), spreading fertiliser. This advert will be targeted at farmers in our service area, Our customers are mainly dairy and cow farmers and our services are aimed at increasing their farm productivity. The final design should inform potential and existing customers about our services and the benefits of them. I will attach files of our logo and some existing advertising material for guidance. We would like the ad to feature the blue and green colours in our logo Please feel free to view our website and facebook page to see more about what we do. www.ridgelineaviation.com.au Some text we would like included Spraying: -Accurate -Time Efficient -Zero crop damage -Cost efficient Fertiliser Spreading: -Accurate, Pattern-tested equipment -Zero crop damage or wheel marks -Ability to load product out of a truck, bin or bulk bags -Cost effective, Prices from $32 per hectare depending on spread rate The final advert size should be 195 mm wide x 186 mm high Thanks :)

Farmers, Agriculture Industry

Agribusiness

Designer to choose colors to be used in the design.

• Phone number 0491 736 058
• The text included in the decription, or variations of this

```html
<!DOCTYPE html>
<html lang="en">
<head>
<meta charset="utf-8">
<title>Ridgeline Aviation – Agricultural Helicopter Services</title>
<link rel="stylesheet" href="https://fonts.googleapis.com/css2?family=Montserrat:ital,wght@0,800;1,900&family=Roboto+Condensed:wght@400&display=swap">
<style>
  :root {
    --brand-green: #8dc63f;
    --brand-blue: #1b75bc;
    --ink: #1a1a1a;
    --white: #ffffff;
    --sky: #b9cfe0;
    --grass: #66743f;
  }
  * { margin: 0; padding: 0; box-sizing: border-box; }
  html, body { width: 1200px; height: 1200px; overflow: hidden; background: var(--white); }
  .ad { position: relative; width: 1200px; height: 1200px; overflow: hidden; background: var(--white); }
  .ad-art { position: absolute; inset: 0; width: 1200px; height: 1200px; }
  .headline {
    position: absolute; left: 0; width: 1200px; text-align: center;
    font-family: "Montserrat", sans-serif; font-weight: 900; font-style: italic;
    line-height: 1; letter-spacing: 1px;
  }
  .headline-main { top: 30px; font-size: 66px; color: var(--brand-green); }
  .headline-sub { top: 114px; font-size: 64px; color: var(--brand-blue); }
  .headline-rule { position: absolute; top: 144px; height: 2px; background: var(--ink); }
  .rule-left { left: 123px; width: 288px; }
  .rule-right { left: 797px; width: 290px; }
  .brand-name {
    position: absolute; left: 56px; top: 522px; width: 380px; text-align: center;
    font-family: "Montserrat", sans-serif; font-weight: 800; font-size: 34px;
    line-height: 1.05; color: var(--brand-blue);
  }
  .section-tab {
    position: absolute; left: 0; height: 60px; background: var(--brand-blue);
    border-radius: 0 30px 30px 0; padding-left: 34px;
    font-family: "Montserrat", sans-serif; font-weight: 900; font-style: italic;
    font-size: 50px; line-height: 60px; color: var(--brand-green);
  }
  .tab-spraying { top: 713px; width: 312px; }
  .tab-spreading { top: 874px; width: 341px; }
  .benefit {
    position: absolute; top: 795px; display: flex; align-items: center; gap: 14px;
    font-family: "Roboto Condensed", sans-serif; font-size: 39px; color: var(--ink);
  }
  .benefit svg { width: 34px; height: 30px; }
  .feature {
    position: absolute; font-family: "Roboto Condensed", sans-serif; font-size: 29px;
    line-height: 37px; color: var(--ink);
  }
  .feature::before {
    content: ""; position: absolute; left: -22px; top: 10px; width: 16px; height: 16px;
    border-radius: 50%; background: var(--brand-blue);
  }
  .footer-line { position: absolute; left: 0; top: 1101px; width: 1200px; height: 11px; background: var(--brand-green); }
  .footer { position: absolute; left: 0; top: 1112px; width: 1200px; height: 88px; background: var(--brand-blue); }
  .footer-item {
    position: absolute; top: 20px; display: flex; align-items: center; gap: 18px;
    font-family: "Roboto Condensed", sans-serif; font-size: 40px; line-height: 48px; color: var(--white);
  }
  .footer-item svg { width: 46px; height: 46px; }
  .footer-phone { left: 128px; }
  .footer-web { left: 612px; }
  .footer-divider { position: absolute; left: 550px; top: 30px; width: 3px; height: 28px; background: var(--white); }
</style>
</head>
<body>
<main class="ad">
  <svg class="ad-art" viewBox="124 157 1282 1221" preserveAspectRatio="none" aria-hidden="false">
    <defs>
      <linearGradient id="photoTone" x1="0" y1="0" x2="0" y2="1">
        <stop offset="0" stop-color="#ffffff"/>
        <stop offset="0.22" stop-color="#c7d8e6"/>
        <stop offset="0.55" stop-color="#e4eaee"/>
        <stop offset="0.66" stop-color="#8a9566"/>
        <stop offset="1" stop-color="#5f6d3f"/>
      </linearGradient>
      <linearGradient id="fieldTone" x1="0" y1="0" x2="0" y2="1">
        <stop offset="0" stop-color="#ffffff"/>
        <stop offset="0.4" stop-color="#eef0ef"/>
        <stop offset="1" stop-color="#f6f7f6"/>
      </linearGradient>
    </defs>
    <rect class="field-backdrop" x="124" y="840" width="1282" height="440" fill="url(#fieldTone)" role="img" aria-label="Faded farmland landscape"/>
    <path class="hero-photo" role="img" aria-label="Helicopter with spray boom applying spray over green pasture under a cloudy sky"
          d="M124,340 L1406,340 L1406,700 C1100,860 800,860 560,790 L300,610 C230,580 170,520 124,450 Z"
          fill="url(#photoTone)"/>
    <path class="swoosh-blue" d="M110,482 C170,565 220,610 300,630" fill="none" stroke="var(--brand-blue)" stroke-width="34"/>
    <path class="swoosh-green" d="M110,442 C170,520 230,575 300,598" fill="none" stroke="var(--brand-green)" stroke-width="24"/>
    <path class="swoosh-blue" d="M500,812 C760,935 1080,935 1430,745" fill="none" stroke="var(--brand-blue)" stroke-width="48"/>
    <path class="swoosh-green" d="M540,795 C770,870 1060,880 1430,703" fill="none" stroke="var(--brand-green)" stroke-width="26"/>
    <ellipse class="badge-outer" cx="387" cy="718" rx="233" ry="127" fill="var(--brand-blue)"/>
    <ellipse class="badge-ring" cx="387" cy="718" rx="218" ry="113" fill="var(--brand-green)"/>
    <ellipse class="badge-inner" cx="387" cy="718" rx="210" ry="105" fill="var(--white)"/>
  </svg>

  <h1 class="headline headline-main">AGRICULTURAL HELICOPTER</h1>
  <span class="headline-rule rule-left"></span>
  <h2 class="headline headline-sub">SERVICES</h2>
  <span class="headline-rule rule-right"></span>

  <div class="brand-name">Ridgeline<br>Aviation</div>

  <div class="section-tab tab-spraying">Spraying:</div>
  <div class="benefit" style="left:29px"><svg viewBox="0 0 34 30"><rect x="2" y="8" width="22" height="20" fill="none" stroke="var(--brand-green)" stroke-width="3"/><path d="M7,16 L13,23 L31,3" fill="none" stroke="var(--brand-green)" stroke-width="5"/></svg>Accurate</div>
  <div class="benefit" style="left:254px"><svg viewBox="0 0 34 30"><rect x="2" y="8" width="22" height="20" fill="none" stroke="var(--brand-green)" stroke-width="3"/><path d="M7,16 L13,23 L31,3" fill="none" stroke="var(--brand-green)" stroke-width="5"/></svg>Time efficient</div>
  <div class="benefit" style="left:553px"><svg viewBox="0 0 34 30"><rect x="2" y="8" width="22" height="20" fill="none" stroke="var(--brand-green)" stroke-width="3"/><path d="M7,16 L13,23 L31,3" fill="none" stroke="var(--brand-green)" stroke-width="5"/></svg>Zero crop damage</div>
  <div class="benefit" style="left:914px"><svg viewBox="0 0 34 30"><rect x="2" y="8" width="22" height="20" fill="none" stroke="var(--brand-green)" stroke-width="3"/><path d="M7,16 L13,23 L31,3" fill="none" stroke="var(--brand-green)" stroke-width="5"/></svg>Cost-effective</div>

  <div class="section-tab tab-spreading">Spreading:</div>
  <p class="feature" style="left:73px; top:946px">Accurate, Pattern-tested equipment</p>
  <p class="feature" style="left:73px; top:1004px">Ability to load out of a Truck, Bin or bulk-bags</p>
  <p class="feature" style="left:663px; top:946px">Zero crop damage or wheel marks</p>
  <p class="feature" style="left:663px; top:1004px">Competitive Prices (from $32 per<br>hectare depending on spread rate)</p>

  <div class="footer-line"></div>
  <footer class="footer">
    <div class="footer-item footer-phone">
      <svg viewBox="0 0 46 46"><circle cx="23" cy="23" r="20" fill="none" stroke="var(--white)" stroke-width="3"/><path d="M16,12 L20,12 L22,18 L19,20 C20,24 22,26 26,27 L28,24 L34,26 L34,30 C34,32 32,33 30,33 C21,32 14,25 13,16 C13,14 14,12 16,12 Z" fill="var(--white)"/></svg>
      0491 736 058
    </div>
    <span class="footer-divider"></span>
    <div class="footer-item footer-web">
      <svg viewBox="0 0 46 46" fill="none" stroke="var(--white)" stroke-width="2.5"><circle cx="23" cy="23" r="19"/><ellipse cx="23" cy="23" rx="9" ry="19"/><line x1="4" y1="23" x2="42" y2="23"/><path d="M7,13 H39 M7,33 H39"/></svg>
      www.ridgelineaviation.com.au
    </div>
  </footer>
</main>
</body>
</html>
```